Cover for "ROOTED! The skill and rhythm of guiding teams through calm and delight"

My first book for a global audience of modern performance leaders needs its cover!
I am an international executive coach and I've developed a new approach to replace classic Performance Management with a natural, sustainable approach fit for human beings :) My first book is about this approach and serves two purposes: helping leaders and sparking their curiosity to learn more, and positioning myself as a thought leader in the field.
The book is built on personal experience; it is both professional and personal ("From me to You"), and I'd like to position it beyond classic categorisation.
Its cover should communicate humanness, naturalness, ease and joy, within an unmistakably business-y context. I would like to see designs that use the color yellow (but not sure it communicates the right things).
Updates

Target Market(s)

Leaders who aspire to have a positive impact and deliver results in a meaningful way

Industry/Entity Type

Consulting & Executive Coaching - Trusted Advisor

Font styles to use
Other font styles liked:
• Helvetica Neue

Colors
0094D4
00A9DD
6FCCEA
C7EBF8
E9F6FB
FFC000
F8CF3A
FAE287
FDF2CF
FEFAEE
EE7325
F08F49
F5BC92
FAE3D3
FDF4ED

Requirements
Must have
• A both-and feeling to it (see description), e.g., masculine AND feminine, business AND humanness. Power with, not power over...
Should not have
• Too much "bling" - no classic status symbol business success language

```html
<!DOCTYPE html>
<html lang="en">
<head>
<meta charset="utf-8">
<title>ROOTED! Book Cover</title>
<link rel="stylesheet" href="https://fonts.googleapis.com/css2?family=Playfair+Display:wght@400&family=Oranienbaum&family=Poppins:wght@600&display=swap">
<style>
  :root {
    --backdrop: #1f6e8f;
    --sea-deep: #1d4f72;
    --sea-green: #3f7c74;
    --foam: #dfe9ee;
    --coral: #ee716d;
    --white: #ffffff;
  }
  html, body {
    margin: 0;
    padding: 0;
    width: 1200px;
    height: 1200px;
    overflow: hidden;
    background: var(--backdrop);
  }
  .book-cover {
    position: absolute;
    left: 271px;
    top: 108px;
    width: 658px;
    height: 985px;
    box-shadow: 0 10px 28px rgba(0, 20, 40, 0.35);
  }
  .book-cover svg { display: block; }
  .cover-title {
    font-family: "Playfair Display", Georgia, serif;
    font-weight: 400;
    fill: var(--white);
    fill-opacity: 0.88;
  }
  .cover-author {
    font-family: "Oranienbaum", "Playfair Display", serif;
    fill: var(--white);
  }
  .cover-subtitle {
    font-family: "Poppins", "Helvetica Neue", Arial, sans-serif;
    font-weight: 600;
    fill: var(--white);
  }
</style>
</head>
<body>
  <div class="book-cover">
    <svg width="658" height="985" viewBox="0 0 658 985" xmlns="http://www.w3.org/2000/svg">
      <defs>
        <linearGradient id="sea-base" x1="0" y1="0" x2="0" y2="1">
          <stop offset="0" stop-color="#3a6f8c"/>
          <stop offset="0.3" stop-color="#5a8a8f"/>
          <stop offset="0.55" stop-color="#3f7c74"/>
          <stop offset="0.8" stop-color="#2c6787"/>
          <stop offset="1" stop-color="#1d4f72"/>
        </linearGradient>
        <radialGradient id="sea-foam" cx="0.45" cy="0.38" r="0.5">
          <stop offset="0" stop-color="#dfe9ee" stop-opacity="0.55"/>
          <stop offset="1" stop-color="#dfe9ee" stop-opacity="0"/>
        </radialGradient>
      </defs>

      <g role="img" aria-label="Photograph of a rowing crew of four in a long boat on a rough, foaming ocean beneath a breaking wave">
        <rect class="sea-photo" width="658" height="985" fill="url(#sea-base)"/>
        <rect width="658" height="985" fill="url(#sea-foam)"/>
      </g>

      <text class="cover-title" transform="translate(44,27) rotate(90)" x="0" y="0"
            font-size="247" textLength="912" lengthAdjust="spacingAndGlyphs">ROOTED!</text>

      <rect class="subtitle-box" x="150" y="264" width="358" height="144" fill="var(--coral)"/>
      <text class="cover-subtitle" text-anchor="middle" font-size="19">
        <tspan x="330" y="315">The Skill and Rhythm</tspan>
        <tspan x="330" y="341">of Guiding Teams through</tspan>
        <tspan x="330" y="368">Calm and Delight</tspan>
      </text>

      <text class="cover-author" x="178" y="192" font-size="60"
            textLength="302" lengthAdjust="spacingAndGlyphs">Marta Holmqvist</text>
    </svg>
  </div>
</body>
</html>
```